Corvane Solutions Website

Corvane Solutions (CS) provide Analytics & Enterprise Performance Management (EPM) advisory & consultancy services. We are passionate about data and making a difference for our clients by working in partnership with them, helping them on their journey to becoming an Corvane Solution. We deliver insights which give our clients a competitive edge and a much deeper understanding of their organisation.

We need a website which shows who we are, what we do and how we do it.

www.corvane-solutions.com is our very basic website at the moment. We want to completely revamp it with a corporate look

```html
<!DOCTYPE html>
<html lang="en">
<head>
<meta charset="utf-8">
<title>Corvane Solutions</title>
<link href="https://fonts.googleapis.com/css2?family=Montserrat:wght@400;500;600;700;800&display=swap" rel="stylesheet">
<style>
:root{
  --navy:#2c4a63;
  --navy-deep:#1f3a52;
  --ink:#1c1c1e;
  --body:#555b61;
  --mist:#eef2f6;
  --ghost:#e7ecf0;
  --ring:#e8edf1;
  --white:#ffffff;
  --line:#cfd5da;
}
*{box-sizing:border-box;margin:0;padding:0}
html,body{width:1200px;height:3522px;overflow:hidden}
body{font-family:'Montserrat',sans-serif;color:var(--ink);background:var(--white);position:relative}
section,footer{position:absolute;left:0;width:1200px}
.abs{position:absolute}

/* Hero */
.hero{top:0;height:672px;background:linear-gradient(180deg,#3e6b8f 0%,#6f98b8 28%,#9fb8c7 45%,#8a8577 58%,#6d7c86 72%,#b99a6a 85%,#5d7f99 100%)}
.hero-photo{position:absolute;inset:0}
.hero-shade{position:absolute;inset:0;background:linear-gradient(180deg,rgba(20,40,60,.35),rgba(20,40,60,.05) 50%,rgba(20,40,60,.1))}
.brand{display:flex;align-items:center;gap:16px}
.brand-dot{width:72px;height:72px;border-radius:50%;border:11px solid var(--white)}
.brand-name{font-weight:700;font-size:28px;line-height:32px;letter-spacing:.5px;color:var(--white)}
.hero .brand{left:112px;top:22px}
.nav{right:110px;top:54px;display:flex;gap:30px}
.nav a{color:var(--white);text-decoration:none;font-weight:700;font-size:17px}
.hero-title{left:0;width:1200px;top:176px;text-align:center;color:var(--white);font-weight:700;font-size:66px;letter-spacing:1px}
.hero-sub{left:0;width:1200px;top:264px;text-align:center;color:var(--white);font-weight:500;font-size:29px}
.btn-solid{left:496px;top:331px;width:208px;height:64px;background:var(--white);color:var(--ink);font-weight:500;font-size:20px;display:flex;align-items:center;justify-content:center}

/* Section headings */
.ghost{color:var(--ghost);font-weight:800;font-size:70px;letter-spacing:1px;white-space:nowrap}
.center{left:0;width:1200px;text-align:center}
.h2{font-weight:700;font-size:41px;color:var(--ink)}
.btn-outline{border:1.5px solid #3b3b3b;font-weight:500;font-size:18px;color:var(--ink);display:flex;align-items:center;justify-content:center;background:transparent}

/* About */
.about{top:672px;height:644px}
.about-disc{left:75px;top:63px;width:520px;height:520px;border-radius:50%;background:var(--navy)}
.about-inner{left:170px;top:135px;width:430px;height:430px;border-radius:50%;background:#e6ebee}
.laptop{left:28px;top:80px;width:635px;height:365px;background:linear-gradient(160deg,#cfd6dc,#5f7a8e 40%,#a9b7c1 80%,#e3e7ea);border-radius:10px;transform:skewY(8deg)}
.about-ghost{left:666px;top:82px}
.welcome{left:673px;top:164px;font-weight:600;font-size:30px}
.about-name{left:673px;top:200px;font-weight:700;font-size:41px;line-height:48px}
.about-text{left:673px;top:316px;width:420px;font-size:17.5px;line-height:26.6px;color:var(--body)}
.about .btn-outline{left:672px;top:478px;width:154px;height:57px}

/* Services */
.services{top:1316px;height:697px;background:var(--mist)}
.services .ghost{top:60px}
.services .h2{top:132px}
.card{top:215px;width:311px;height:400px;background:var(--white);border-radius:8px;box-shadow:0 4px 14px rgba(40,70,100,.08);text-align:center}
.card svg{position:absolute;left:110px;top:20px}
.card-title{position:absolute;left:0;width:100%;top:130px;font-weight:500;font-size:25px}
.card-text{position:absolute;left:22px;width:267px;top:174px;font-size:17px;line-height:23px;color:var(--body)}
.card .btn-outline{position:absolute;left:79px;top:310px;width:153px;height:58px}

/* Process */
.process{top:2013px;height:569px}
.process .ghost{top:75px}
.process .h2{top:146px}
.step{top:228px;width:260px;text-align:center}
.step svg{display:block;margin:0 auto}
.step-label{margin-top:16px;font-weight:500;font-size:23px;line-height:31px}

/* Contact */
.contact{top:2582px;height:557px;background:linear-gradient(135deg,#42647f 0%,#36576f 50%,#3f627e 100%)}
.contact .ghost{top:55px;color:rgba(255,255,255,.18)}
.contact .h2{top:128px;color:var(--white)}
.field{background:#fafafa;border-radius:3px;font-size:16px;color:#444;padding:14px 18px}
.contact .submit{left:538px;top:425px;width:123px;height:60px;border:1.5px solid rgba(255,255,255,.8);color:var(--white);font-weight:600;font-size:19px;display:flex;align-items:center;justify-content:center}

/* Footer */
.footer{top:3139px;height:383px;background:var(--white)}
.footer .brand{left:112px;top:72px}
.footer .brand-dot{width:104px;height:104px;border:16px solid var(--navy)}
.footer .brand-name{color:var(--navy);font-size:35px;line-height:40px}
.partner-badge{left:112px;top:196px;width:262px;height:58px;background:#d9dfe4;border-radius:4px}
.f-col h4{font-weight:500;font-size:19px;margin-bottom:20px}
.f-col a,.f-col p{display:block;font-size:16px;color:var(--body);text-decoration:none;line-height:20px;margin-bottom:10px}
.f-info{left:585px;top:68px}
.f-contact{left:782px;top:68px}
.f-row{display:flex;gap:8px;align-items:flex-start;margin-bottom:26px;font-size:16px;color:var(--body);line-height:23px}
.f-row svg{flex:none;margin-top:4px}
.f-rule{left:112px;top:291px;width:976px;height:1px;background:var(--line)}
.copyright{left:112px;top:324px;font-size:16px;color:var(--body)}
.social{top:314px;width:38px;height:38px;border-radius:50%;border:1.5px solid var(--navy)}
</style>
</head>
<body>

<section class="hero">
  <div class="hero-photo" role="img" aria-label="Photograph of a city riverfront with modern office buildings and a harp-shaped cable bridge reflected in the water"></div>
  <div class="hero-shade"></div>
  <div class="abs brand"><span class="brand-dot"></span><span class="brand-name">CORVANE<br>SOLUTIONS</span></div>
  <nav class="abs nav"><a href="#">HOME</a><a href="#">ABOUT US</a><a href="#">SERVICES</a><a href="#">CONTACT US</a></nav>
  <h1 class="abs hero-title">CORVANE SOLUTIONS</h1>
  <p class="abs hero-sub">Analytics &nbsp;|&nbsp; EPM advisory &nbsp;|&nbsp; Consultancy Services</p>
  <a class="abs btn-solid">GET MORE INFO</a>
</section>

<section class="about">
  <div class="abs about-disc"></div>
  <div class="abs about-inner"></div>
  <div class="abs laptop" role="img" aria-label="Photograph of a laptop showing an analytics dashboard with charts"></div>
  <div class="abs ghost about-ghost">WHO WE ARE</div>
  <p class="abs welcome">WELCOME TO</p>
  <h2 class="abs about-name">CORVANE<br>SOLUTIONS</h2>
  <p class="abs about-text">Corvane Solutions is an exciting start-up in the Data Analytics and EPM space.&nbsp; Founded in 2019, CS specialise in the implementation and support of BI, EPM and Data Analytics business solutions, both in the Cloud and on-premise.</p>
  <a class="abs btn-outline">READ MORE</a>
</section>

<section class="services">
  <div class="abs ghost center">WHAT WE DO</div>
  <h2 class="abs h2 center">OUR SERVICES</h2>

  <div class="abs card" style="left:112px">
    <svg width="90" height="90" viewBox="0 0 90 90" fill="none" stroke="#2c4a63" stroke-width="3"><rect x="8" y="16" width="74" height="52" rx="3"/><path d="M2 72h86"/><circle cx="30" cy="36" r="7"/><path d="M18 62c2-10 22-10 24 0"/><path d="M50 34h22M50 44h22M50 54h16"/><circle cx="62" cy="10" r="7"/></svg>
    <h3 class="card-title">Advise &amp; Architect</h3>
    <p class="card-text">Helping our customers understand the art of the possible and safeguarding their investments by overseeing implementations.</p>
    <a class="btn-outline">READ MORE</a>
  </div>

  <div class="abs card" style="left:444px">
    <svg width="90" height="90" viewBox="0 0 90 90" fill="none" stroke="#2c4a63" stroke-width="3"><circle cx="45" cy="45" r="11"/><circle cx="45" cy="45" r="22" stroke-dasharray="6 6"/><path d="M6 70h14l14 6h18M62 8l18 4v14"/><rect x="2" y="64" width="10" height="16"/><rect x="76" y="6" width="10" height="16"/></svg>
    <h3 class="card-title">Design &amp; Implement</h3>
    <p class="card-text">Working with the project management team, through each stage of the project, with clearly defined deliverables and well exercised plans to deliver them.</p>
    <a class="btn-outline">READ MORE</a>
  </div>

  <div class="abs card" style="left:776px">
    <svg width="90" height="90" viewBox="0 0 90 90" fill="none" stroke="#2c4a63" stroke-width="3"><circle cx="45" cy="34" r="24" stroke-dasharray="5 3"/><circle cx="26" cy="62" r="20"/><circle cx="64" cy="62" r="20"/><path d="M26 52v20M64 52v10l6 6"/></svg>
    <h3 class="card-title">Optimise &amp; Manage</h3>
    <p class="card-text">Our Managed Services delivers proactive, on-demand support for EPM and Data Analytics environments:</p>
    <a class="btn-outline">READ MORE</a>
  </div>
</section>

<section class="process">
  <div class="abs ghost center">HOW WE DO IT</div>
  <h2 class="abs h2 center">OUR PROCESS</h2>

  <div class="abs step" style="left:82px">
    <svg width="200" height="190" viewBox="0 0 200 190"><path d="M100 8a86 86 0 1 1-70 136" fill="none" stroke="#e8edf1" stroke-width="18"/><circle cx="56" cy="70" r="20" fill="#eef1f4"/><text x="56" y="78" text-anchor="middle" font-family="Montserrat,sans-serif" font-weight="700" font-size="22" fill="#1c1c1e">1</text><g fill="none" stroke="#2c4a63" stroke-width="3"><rect x="96" y="66" width="40" height="50"/><path d="M103 80h26M103 90h14M118 108l12-14"/><circle cx="90" cy="72" r="12"/></g></svg>
    <p class="step-label">Business Planning<br>And Budgeting</p>
  </div>

  <div class="abs step" style="left:340px">
    <svg width="200" height="190" viewBox="0 0 200 190"><path d="M100 8a86 86 0 1 1-70 136" fill="none" stroke="#e8edf1" stroke-width="18"/><circle cx="56" cy="70" r="20" fill="#eef1f4"/><text x="56" y="78" text-anchor="middle" font-family="Montserrat,sans-serif" font-weight="700" font-size="22" fill="#1c1c1e">2</text><g fill="none" stroke="#2c4a63" stroke-width="3"><rect x="80" y="64" width="54" height="44"/><path d="M88 100v-8M96 100v-14M104 100v-10M90 80l14-6 10 4 12-10"/><circle cx="126" cy="108" r="14"/><circle cx="126" cy="108" r="6"/></g></svg>
    <p class="step-label">Business Analysis &amp;<br>Management Report</p>
  </div>

  <div class="abs step" style="left:598px">
    <svg width="200" height="190" viewBox="0 0 200 190"><path d="M100 8a86 86 0 1 1-70 136" fill="none" stroke="#e8edf1" stroke-width="18"/><circle cx="56" cy="70" r="20" fill="#eef1f4"/><text x="56" y="78" text-anchor="middle" font-family="Montserrat,sans-serif" font-weight="700" font-size="22" fill="#1c1c1e">3</text><g fill="none" stroke="#2c4a63" stroke-width="3"><circle cx="92" cy="70" r="14" stroke-dasharray="5 3"/><circle cx="92" cy="70" r="5"/><path d="M110 64c16 2 24 14 22 28M86 92c2 14 12 22 26 22"/><circle cx="128" cy="108" r="11"/><path d="M124 122h8"/></g></svg>
    <p class="step-label">Strategy<br>Management</p>
  </div>

  <div class="abs step" style="left:857px">
    <svg width="200" height="190" viewBox="0 0 200 190"><path d="M100 8a86 86 0 1 1-70 136" fill="none" stroke="#e8edf1" stroke-width="18"/><circle cx="56" cy="70" r="20" fill="#eef1f4"/><text x="56" y="78" text-anchor="middle" font-family="Montserrat,sans-serif" font-weight="700" font-size="22" fill="#1c1c1e">4</text><g fill="none" stroke="#2c4a63" stroke-width="3"><circle cx="114" cy="82" r="30"/><path d="M122 70c-4-4-16-4-16 4s16 4 16 12-12 8-16 4M114 62v40"/><rect x="78" y="100" width="10" height="22"/><path d="M88 104l10-10 4 4-2 8h10v14H88"/></g></svg>
    <p class="step-label">Profitability And<br>Cost Management</p>
  </div>
</section>

<section class="contact" role="img" aria-label="Dark blue tinted photograph of people reviewing printed charts at a desk">
  <div class="abs ghost center">GET IN TOUCH</div>
  <h2 class="abs h2 center">CONTACT US</h2>
  <div class="abs field" style="left:184px;top:216px;width:410px;height:48px">Name</div>
  <div class="abs field" style="left:184px;top:276px;width:410px;height:48px">Email</div>
  <div class="abs field" style="left:184px;top:336px;width:410px;height:48px">Phone Number</div>
  <div class="abs field" style="left:606px;top:216px;width:410px;height:168px">Message</div>
  <a class="abs submit">SUBMIT</a>
</section>

<footer class="footer">
  <div class="abs brand"><span class="brand-dot"></span><span class="brand-name">CORVANE<br>SOLUTIONS</span></div>
  <div class="abs partner-badge" role="img" aria-label="Technology partner badge"></div>

  <div class="abs f-col f-info">
    <h4>Information</h4>
    <a href="#">Home</a><a href="#">About Us</a><a href="#">Services</a><a href="#">Contact Us</a>
  </div>

  <div class="abs f-col f-contact">
    <h4>Contact Us</h4>
    <div class="f-row"><svg width="12" height="16" viewBox="0 0 12 16"><path d="M6 0a6 6 0 0 0-6 6c0 4.5 6 10 6 10s6-5.5 6-10a6 6 0 0 0-6-6zm0 8.5A2.5 2.5 0 1 1 6 3.5a2.5 2.5 0 0 1 0 5z" fill="#2c4a63"/></svg><span>14 Harbour Row,<br>Quayside, Dublin 4, D04 KT21</span></div>
    <div class="f-row"><svg width="14" height="14" viewBox="0 0 14 14"><path d="M3 0l3 3-2 2c1 2 3 4 5 5l2-2 3 3-2 3C6 14 0 8 0 3z" fill="#2c4a63"/></svg><span>01 480 2715</span></div>
    <div class="f-row"><svg width="16" height="12" viewBox="0 0 16 12"><rect width="16" height="12" rx="1" fill="#2c4a63"/><path d="M1 1l7 6 7-6" stroke="#fff" stroke-width="1.4" fill="none"/></svg><span>info@corvane-solutions.com</span></div>
  </div>

  <div class="abs f-rule"></div>
  <p class="abs copyright">Copyright © 2022, Corvane Solutions. All rights reserved.</p>
  <span class="abs social" style="left:1004px"></span>
  <span class="abs social" style="left:1050px"></span>
</footer>

</body>
</html>
```